Business Card Design needed for start up company Pramora

In need of a new business card designed for a start up company based in Sydney, Pramora is a new start up innovative Company, our mission it to make property accessible for everyday Australian and to become the leading Real Estate platform in Australia. We want it to be fresh and clean.

Industry/Entity Type

Financial

Contact Information for Business Card

Section for Name
Section for Title

PRAMORA - Where Doors Open Wide
Mobile:
Direct:

Font styles to use
Sans Serif

Colors
33a6d7
0692cd
0255a3
ffffff

Requirements
Must have
• Logo, all business card details

```html
<!DOCTYPE html>
<html lang="en">
<head>
<meta charset="utf-8">
<title>Pramora Business Card</title>
<link href="https://fonts.googleapis.com/css2?family=Lato:wght@400;700;900&display=swap" rel="stylesheet">
<style>
  :root {
    --navy: #1d4a85;
    --deep-blue: #0255a3;
    --brand-blue: #2199d6;
    --sky-blue: #33a6d7;
    --white: #ffffff;
    --backdrop: #e9ecef;
    --card-shadow: 0 14px 30px rgba(0, 0, 0, 0.18);
  }
  * { box-sizing: border-box; margin: 0; padding: 0; }
  html, body {
    width: 1200px;
    height: 880px;
    overflow: hidden;
    background: var(--backdrop);
    font-family: "Lato", sans-serif;
  }
  .stage { position: relative; width: 1200px; height: 880px; }
  .card {
    position: absolute;
    width: 600px;
    height: 343px;
    background: var(--white);
    box-shadow: var(--card-shadow);
    overflow: hidden;
  }
  .card-front { left: 70px; top: 70px; }
  .card-back { left: 530px; top: 467px; }

  .brand { display: flex; align-items: center; gap: 14px; }
  .brand-dot {
    border-radius: 50%;
    background: var(--brand-blue);
    flex: none;
  }
  .brand-name {
    font-family: "Lato", sans-serif;
    font-weight: 900;
    color: var(--navy);
    letter-spacing: -0.5px;
    line-height: 1;
  }
  .card-front .brand {
    position: absolute;
    left: 50%;
    top: 50%;
    transform: translate(-50%, -50%);
  }
  .card-front .brand-dot { width: 96px; height: 96px; }
  .card-front .brand-name { font-size: 68px; }

  .back-tab {
    position: absolute;
    left: 40px; top: 0;
    width: 88px; height: 60px;
    background: var(--navy);
  }
  .back-disc {
    position: absolute;
    left: 380px; top: -90px;
    width: 360px; height: 360px;
    border-radius: 50%;
    background: var(--brand-blue);
  }
  .card-back .brand { position: absolute; left: 44px; top: 46px; }
  .card-back .brand-dot { width: 84px; height: 84px; }
  .card-back .brand-name { font-size: 50px; margin-top: -18px; }

  .person { position: absolute; left: 48px; top: 182px; }
  .person-name { font-weight: 700; font-size: 20px; color: var(--navy); }
  .person-title { font-weight: 400; font-size: 15px; color: var(--brand-blue); margin-top: 1px; }

  .contacts { position: absolute; left: 48px; top: 240px; list-style: none; }
  .contacts li {
    display: flex; align-items: center; gap: 8px;
    font-size: 16px; color: var(--navy); margin-bottom: 4px;
  }
  .contact-icon { width: 17px; height: 17px; flex: none; }

  .tagline {
    position: absolute; left: 48px; bottom: 22px;
    font-size: 15px; color: var(--navy);
  }
  .tagline strong { font-weight: 900; }
</style>
</head>
<body>
<main class="stage">

  <section class="card card-front" aria-label="Card front">
    <div class="brand">
      <span class="brand-dot"></span>
      <span class="brand-name">PRAMORA</span>
    </div>
  </section>

  <section class="card card-back" aria-label="Card back">
    <div class="back-disc"></div>
    <div class="back-tab"></div>
    <div class="brand">
      <span class="brand-dot"></span>
      <span class="brand-name">PRAMORA</span>
    </div>

    <div class="person">
      <p class="person-name">Liam Carter</p>
      <p class="person-title">Sales Extraordinaire</p>
    </div>

    <ul class="contacts">
      <li>
        <svg class="contact-icon" viewBox="0 0 17 17" aria-label="Mobile">
          <rect width="17" height="17" rx="2" fill="var(--brand-blue)"/>
          <rect x="5.5" y="2.5" width="6" height="12" rx="1" fill="none" stroke="#fff" stroke-width="1.4"/>
          <circle cx="8.5" cy="12.3" r="0.8" fill="#fff"/>
        </svg>
        555.014.2690
      </li>
      <li>
        <svg class="contact-icon" viewBox="0 0 17 17" aria-label="Direct">
          <rect width="17" height="17" rx="2" fill="var(--brand-blue)"/>
          <path d="M3 7 Q8.5 3 14 7 L12.5 9 L10.5 8 L10.5 7 Q8.5 6 6.5 7 L6.5 8 L4.5 9 Z" fill="#fff"/>
          <rect x="4.5" y="10" width="8" height="4" rx="1" fill="#fff"/>
        </svg>
        555.014.2690
      </li>
    </ul>

    <p class="tagline"><strong>PRAMORA</strong> - Where Doors Open Wide</p>
  </section>

</main>
</body>
</html>
```